E Marketing - Vortel Flyer

Our product is an E Marketing campaign for business.We have called the product Vortel. Benefits to Business are:
1. Direct communications to qualified clients;
2. Generate new leads;
2. Drive traffic to your website;
3. Unlimited campaigns.

We want to have a special offer whereby the client signs on for twelve months and recieves two months free. The cost of the product is $550 for the templeate as a one off fee and $90 per month.The designer can deciede whether the cost should feature in the flyer.
Our website for reference is www.brightquillpromo.com.au

Target Market(s)

Business who currently have a website and would like to drive more traffic. Businessess who want to talk directly to thier clients. Business who want to increase sales.

Industry/Entity Type

Marketing

Requirements
Must have
• The brochure should be a single page, not cluttered and clear. It should reflect our corporate colours. The brochure should highlight the name Vortel.

```html
<!DOCTYPE html>
<html lang="en">
<head>
<meta charset="utf-8">
<title>Vortel – Marketing for Growing Business</title>
<link href="https://fonts.googleapis.com/css2?family=Tinos:wght@400;700&family=Arimo:wght@400;700&display=swap" rel="stylesheet">
<style>
  :root {
    --navy: #1c3768;
    --deep-blue: #1f4585;
    --mid-blue: #4f80c2;
    --light-blue: #a9c6ea;
    --pale: #eef4fb;
    --white: #ffffff;
    --text-dark: #1b2c4f;
    --green: #6ebe4a;
    --grey-text: #4d5562;
    --phone-bg: rgba(60, 66, 80, 0.82);
  }
  * { box-sizing: border-box; margin: 0; padding: 0; }
  html, body { width: 939px; height: 1200px; overflow: hidden; background: var(--white); }
  .flyer {
    position: relative;
    width: 939px;
    height: 1200px;
    overflow: hidden;
    font-family: "Tinos", "Times New Roman", serif;
  }
  .sunburst {
    position: absolute; inset: 0;
    background:
      radial-gradient(ellipse 520px 420px at 0 1200px, rgba(255,255,255,1) 0, rgba(255,255,255,0.95) 55%, rgba(255,255,255,0) 100%),
      radial-gradient(circle at 300px 700px, rgba(31,69,133,0.9) 0, rgba(79,128,194,0.75) 420px, rgba(169,198,234,0.35) 760px, rgba(255,255,255,0) 1000px),
      linear-gradient(160deg, var(--deep-blue) 0%, var(--mid-blue) 45%, var(--light-blue) 72%, var(--pale) 100%);
  }
  .brand-title {
    position: absolute; left: 168px; top: 40px;
    font-size: 74px; font-weight: 400; color: var(--white); letter-spacing: 2px; line-height: 1;
  }
  .tagline {
    position: absolute; left: 168px; top: 140px;
    font-size: 36px; color: var(--white); line-height: 1;
  }
  .intro-panel {
    position: absolute; left: 200px; top: 190px; width: 686px; height: 228px;
    background: rgba(215, 230, 248, 0.72);
    border: 3px solid rgba(255,255,255,0.85);
    border-radius: 10px;
    padding: 18px 24px;
    color: var(--text-dark);
    font-size: 17.5px; line-height: 1.4;
  }
  .intro-panel .benefits-heading { margin-top: 14px; }
  .benefit-list {
    list-style: none;
    display: grid; grid-template-columns: 1.55fr 1fr;
    row-gap: 8px; margin-top: 10px; padding-left: 46px;
  }
  .benefit-list li { position: relative; padding-left: 20px; }
  .benefit-list li::before {
    content: ""; position: absolute; left: 0; top: 7px;
    width: 10px; height: 10px; border-radius: 50%; background: var(--green);
  }
  .offer-panel {
    position: absolute; left: 581px; top: 511px; width: 275px; height: 120px;
    background: rgba(140, 175, 225, 0.45);
    border: 3px solid rgba(255,255,255,0.8);
    border-radius: 10px;
    text-align: center; color: var(--white);
    font-size: 21px; line-height: 1.4; padding-top: 16px;
  }
  .offer-panel .offer-rule {
    width: 230px; height: 2px; background: var(--white); margin: 10px auto 0;
  }
  .phone-badge {
    position: absolute; left: 592px; top: 618px; width: 261px; height: 58px;
    background: var(--phone-bg); border-radius: 4px;
    display: flex; align-items: center; padding-left: 14px; gap: 14px;
    color: var(--white); font-family: "Arimo", Arial, sans-serif;
  }
  .phone-badge .phone-number { font-size: 24px; font-weight: 700; line-height: 1; }
  .phone-badge .phone-hours { font-size: 11px; letter-spacing: 1px; opacity: 0.85; text-align: right; margin-top: 4px; }
  .feature-circle {
    position: absolute; border-radius: 50%;
    background: var(--navy); border: 10px solid var(--white);
    display: flex; align-items: center; justify-content: center; text-align: center;
    color: var(--white); line-height: 1.35; letter-spacing: 1px;
    box-shadow: 0 0 0 2px rgba(28,55,104,0.3);
  }
  .circle-direct { left: 67px; top: 480px; width: 266px; height: 266px; font-size: 32px; }
  .circle-campaigns { left: 338px; top: 682px; width: 230px; height: 230px; font-size: 27px; }
  .circle-leads { left: 575px; top: 835px; width: 194px; height: 194px; font-size: 26px; }
  .company-mark {
    position: absolute; left: 53px; top: 930px;
    display: flex; align-items: center; gap: 12px;
  }
  .company-mark .mark-square { width: 46px; height: 46px; background: var(--mid-blue); }
  .company-mark .company-name {
    font-family: "Arimo", Arial, sans-serif; font-size: 30px; font-weight: 700; color: var(--mid-blue);
  }
  .contact-block {
    position: absolute; left: 53px; top: 1000px;
    font-family: "Arimo", Arial, sans-serif; font-style: normal;
    font-size: 14px; line-height: 1.6; color: var(--grey-text);
  }
  .contact-block .website {
    display: inline-block; margin-top: 6px; padding: 2px 8px;
    background: #8c929c; color: var(--white); border: 1px solid #6d737c;
  }
</style>
</head>
<body>
<div class="flyer">
  <div class="sunburst" role="img" aria-label="Blue sunburst rays radiating across the background"></div>

  <h1 class="brand-title">VORTEL</h1>
  <p class="tagline">Marketing for Growing Business</p>

  <section class="intro-panel">
    <p>Achieve fantastic results by drawing on our network of highly trained professionals. Get on board with one of the cheapest and most effective avenues to drive sales.</p>
    <p class="benefits-heading">Benefits for using Vortel:</p>
    <ul class="benefit-list">
      <li>Direct communications to qualified clients.</li>
      <li>Unlimited campaigns</li>
      <li>Drive traffic to your site</li>
      <li>Generate new leads</li>
    </ul>
  </section>

  <section class="offer-panel">
    <p>Join for 12 months and<br>Get 2 Months FREE!</p>
    <div class="offer-rule"></div>
  </section>

  <div class="phone-badge">
    <svg width="24" height="24" viewBox="0 0 24 24" aria-hidden="true">
      <path fill="#ffffff" d="M6.6 10.8c1.4 2.8 3.8 5.1 6.6 6.6l2.2-2.2c.3-.3.7-.4 1-.2 1.1.4 2.3.6 3.6.6.6 0 1 .4 1 1V20c0 .6-.4 1-1 1C10.6 21 3 13.4 3 4c0-.6.4-1 1-1h3.5c.6 0 1 .4 1 1 0 1.3.2 2.5.6 3.6.1.3 0 .7-.2 1z"/>
    </svg>
    <div>
      <div class="phone-number">03 5550 1842</div>
      <div class="phone-hours">24 HOURS A DAY</div>
    </div>
  </div>

  <div class="feature-circle circle-direct">DIRECT<br>TRAFFIC</div>
  <div class="feature-circle circle-campaigns">UNLIMITED<br>CAMPAIGNS</div>
  <div class="feature-circle circle-leads">NEW<br>LEADS</div>

  <div class="company-mark">
    <span class="mark-square"></span>
    <span class="company-name">Brightquill Promo</span>
  </div>

  <address class="contact-block">
    PO Box 4410, Ashvale Vic 3990<br>
    Tel.: +61 3 5550 1843<br>
    Fax: +61 3 5550 1842<br>
    Email: info@brightquillpromo.com.au<br>
    <span class="website">Website: www.brightquillpromo.com.au</span>
  </address>
</div>
</body>
</html>
```